BOOK COVER for Medical Board Review Exam

I want to create a book cover for my company. I currently have a mobile app, and 3 books to help students pass board exams.

I have created 3 more books but I want to REDESIGN all the covers and brand. What that is going to look like for this project is that I am going to select one design for one fo those books and then we are going to work on the other books based on that design.

I have attached some files so you have an idea of what I am looking for... I will also attach the old designs so you KNOW what to write in the cover and back cover :)

I also prefer if the delivery is in FIGMA since I can have permission to micro-edit some of the stuff for final results. It's important to note that this will be for RVN publishing and the measurement is: 8.5 x 11 inches (29.59 x 27.94 cm).

BRAND COLORS: Twitter Blue, White and some bright color highlights

BUDGET: $50

DEADLINE: 2 weeks

```html
<!DOCTYPE html>
<html lang="en">
<head>
<meta charset="utf-8">
<title>NBDX Part 4 Review – Book Cover</title>
<link rel="stylesheet" href="https://fonts.googleapis.com/css2?family=Fredoka:wght@400;500;600&family=Tinos&display=swap">
<style>
  :root {
    --backdrop: #dcedfa;
    --paper: #ffffff;
    --teal: #3f979b;
    --orange: #f2874f;
    --blue: #1f78c8;
    --sky: #3aa6e8;
    --brand-green: #2d6b3a;
    --white: #ffffff;
  }
  * { margin: 0; padding: 0; box-sizing: border-box; }
  html, body { width: 1200px; height: 856px; overflow: hidden; }
  body { background: var(--backdrop); position: relative; }

  .cover {
    position: absolute; left: 343px; top: 37px;
    width: 514px; height: 792px;
    background: var(--paper);
    overflow: hidden;
  }
  .cover-top { position: absolute; left: 0; top: 0; width: 100%; height: 340px; background: var(--paper); }
  .cover-divider { position: absolute; left: 0; top: 340px; width: 100%; height: 5px; background: var(--orange); }
  .cover-bottom { position: absolute; left: 0; top: 345px; width: 100%; height: 447px; background: var(--teal); }

  .ribbon { position: absolute; left: 35px; width: 466px; }
  .ribbon svg { position: absolute; inset: 0; width: 100%; height: 100%; }
  .ribbon span {
    position: relative; display: flex; align-items: center; justify-content: center;
    height: 100%; color: var(--white);
    font-family: "Fredoka", sans-serif; font-weight: 500; font-size: 26px; letter-spacing: 1px;
  }
  .ribbon-series { top: 27px; height: 58px; }
  .ribbon-subject { top: 376px; height: 56px; }

  .title {
    position: absolute; left: 112px; top: 148px;
    font-family: "Fredoka", sans-serif; font-weight: 500; font-size: 82px; line-height: 1;
    color: var(--blue); letter-spacing: 1px;
  }
  .subtitle {
    position: absolute; left: 115px; top: 238px;
    font-family: "Fredoka", sans-serif; font-weight: 500; font-size: 34px; line-height: 1;
    color: var(--orange); letter-spacing: 1px;
  }
  .spine-art {
    position: absolute; left: 402px; top: 156px; width: 38px; height: 122px;
    background: linear-gradient(180deg, var(--sky), var(--blue));
    border-radius: 16px; opacity: 0.85;
  }

  .contents {
    position: absolute; left: 0; top: 458px; width: 558px; list-style: none; text-align: center;
    font-family: "Tinos", serif; font-size: 26px; line-height: 32px; color: var(--white);
  }

  .wave-art {
    position: absolute; left: 320px; top: 470px; width: 194px; height: 322px;
    background: radial-gradient(ellipse at 100% 100%, rgba(255,255,255,0.35), rgba(255,255,255,0) 70%);
  }

  .publisher {
    position: absolute; left: 0; top: 678px; width: 558px;
    display: flex; align-items: center; justify-content: center; gap: 10px;
    font-family: "Tinos", serif; font-size: 27px; color: var(--brand-green);
  }
  .publisher-mark { width: 16px; height: 16px; background: var(--brand-green); }
</style>
</head>
<body>
  <main class="cover">
    <div class="cover-top"></div>
    <div class="cover-divider"></div>
    <div class="cover-bottom"></div>

    <div class="ribbon ribbon-series">
      <svg viewBox="0 0 466 58" preserveAspectRatio="none" aria-hidden="true">
        <path d="M0 4 Q10 0 20 3 L446 3 Q456 0 466 4 L452 29 L466 54 Q456 58 446 55 L20 55 Q10 58 0 54 L14 29 Z" fill="var(--orange)"/>
      </svg>
      <span>CHIRO BOARD REVIEW</span>
    </div>

    <h1 class="title">NBDX</h1>
    <p class="subtitle">PART 4 REVIEW</p>
    <div class="spine-art" role="img" aria-label="Illustration of a stylised spinal column"></div>

    <div class="ribbon ribbon-subject">
      <svg viewBox="0 0 466 56" preserveAspectRatio="none" aria-hidden="true">
        <path d="M0 4 Q10 0 20 3 L446 3 Q456 0 466 4 L452 28 L466 52 Q456 56 446 53 L20 53 Q10 56 0 52 L14 28 Z" fill="var(--orange)"/>
      </svg>
      <span>CHIROPRACTICE TECHNIQUE</span>
    </div>

    <ul class="contents">
      <li>50+&nbsp; Presentation</li>
      <li>55 + Technique Set-up</li>
      <li>Points Of Performance</li>
      <li>Body landmarks</li>
      <li>Poselogy</li>
    </ul>

    <div class="wave-art" role="img" aria-label="Decorative flowing white line pattern"></div>

    <div class="publisher">
      <span class="publisher-mark"></span>
      <span class="publisher-name">Larkfield.com</span>
    </div>
  </main>
</body>
</html>
```